Brimlock Assurance Branding Revamp

We are a consulting company, looking for a way to display and promote our brand. We have 2 sides to the business- Brimlock (financial) and Assurance (cyber security). The financial side products relate to business necessities: card processing, website design/hosting/maintenance, VoIP phone systems. The cyber security side promotes a bundled package of 4 solutions: network vulnerability scan, dark web scan, anti-ransomeware/malware software, and image-level backups. We want people to understand that partnering with Brimlock Assurance gives them “Elevated Peace of Mind” (tagline). Current badge and logos uploaded.

Target Market(s)

Small businesses

Contact Information for Business Card

Carla Whitfield, Vice President, carla@brimlockassurance.example, 555-384-9106, www.brimlockassurance.example

Requirements
Nice to have
• I do prefer the darker background for front and back

```html
<!DOCTYPE html>
<html lang="en">
<head>
<meta charset="utf-8">
<title>Brimlock Assurance – Business Card</title>
<link rel="stylesheet" href="https://fonts.googleapis.com/css2?family=Montserrat:wght@400;500;700&display=swap">
<style>
  :root {
    --stage: #cfcfcf;
    --stage-dark: #a9a9a9;
    --card-navy: #0f0e38;
    --accent-red: #e3202b;
    --text-white: #ffffff;
    --shadow: rgba(0, 0, 0, 0.35);
  }
  * { box-sizing: border-box; margin: 0; padding: 0; }
  html, body {
    width: 1200px;
    height: 788px;
    overflow: hidden;
  }
  body {
    background: linear-gradient(180deg, var(--stage) 0%, var(--stage-dark) 100%);
    font-family: "Montserrat", Arial, sans-serif;
    display: flex;
    align-items: center;
    justify-content: center;
    gap: 48px;
  }
  .card {
    position: relative;
    width: 528px;
    height: 302px;
    background: var(--card-navy);
    border-radius: 22px;
    border-bottom: 4px solid var(--accent-red);
    box-shadow: 0 14px 28px var(--shadow);
    color: var(--text-white);
    overflow: hidden;
  }
  .brand {
    position: absolute;
    display: flex;
    align-items: center;
    gap: 10px;
    font-weight: 500;
    text-transform: uppercase;
    color: var(--text-white);
    white-space: nowrap;
  }
  .brand-square {
    width: 14px;
    height: 14px;
    background: var(--accent-red);
    flex: none;
  }
  .card-front .brand {
    top: 40px;
    right: 36px;
    font-size: 15px;
    letter-spacing: 0.28em;
  }
  .card-back .brand {
    top: 50%;
    right: 40px;
    transform: translateY(-50%);
    font-size: 19px;
    letter-spacing: 0.3em;
  }
  .identity {
    position: absolute;
    left: 38px;
    bottom: 118px;
  }
  .identity-name {
    color: var(--accent-red);
    font-weight: 700;
    font-size: 24px;
    letter-spacing: 0.02em;
    text-transform: uppercase;
  }
  .identity-title {
    font-size: 15px;
    margin-top: 2px;
  }
  .contact-list {
    position: absolute;
    left: 38px;
    bottom: 26px;
    list-style: none;
    font-size: 14px;
    line-height: 26px;
  }
  .contact-item {
    display: flex;
    align-items: center;
    gap: 10px;
  }
  .contact-icon {
    width: 14px;
    height: 14px;
    fill: none;
    stroke: var(--accent-red);
    stroke-width: 2;
    flex: none;
  }
</style>
</head>
<body>
  <section class="card card-front">
    <div class="brand"><span class="brand-square"></span>Brimlock Assurance</div>

    <div class="identity">
      <h1 class="identity-name">Carla Whitfield</h1>
      <p class="identity-title">Vice President</p>
    </div>

    <ul class="contact-list">
      <li class="contact-item">
        <svg class="contact-icon" viewBox="0 0 16 16" aria-hidden="true"><path d="M4 1.5l2.5 3-1.5 1.5c.8 2 2.5 3.7 4.5 4.5l1.5-1.5 3 2.5-1.5 2.5C7 14 2 9 1.5 3z"/></svg>
        555-384-9106
      </li>
      <li class="contact-item">
        <svg class="contact-icon" viewBox="0 0 16 16" aria-hidden="true"><rect x="1.5" y="3.5" width="13" height="9"/><path d="M1.5 3.5l6.5 5 6.5-5"/></svg>
        carla@brimlockassurance.example
      </li>
      <li class="contact-item">
        <svg class="contact-icon" viewBox="0 0 16 16" aria-hidden="true"><circle cx="8" cy="8" r="6.5"/><path d="M1.5 8h13M8 1.5c-3 3.5-3 9.5 0 13M8 1.5c3 3.5 3 9.5 0 13"/></svg>
        www.brimlockassurance.example
      </li>
    </ul>
  </section>

  <section class="card card-back">
    <div class="brand"><span class="brand-square"></span>Brimlock Assurance</div>
  </section>
</body>
</html>
```